Comparison Website Design for Glue Website

Note: We don't have a logo, it's not needed. Just put placeholder.

We would like a website comparing A to B, simple elegant design, simplistic styling. Website is for helping people find the best glue to glue 2 things together. For example, Metal to wood, Metal to rubber, glass to fabric and so on. Select 2 options and be shown the best glue/adhesive for the job.

Purpose of the website:
Allowing someone to pick 2 materials they want to glue together, and showing them the best product for it. We want someone to select 2 materials like "Metal and Rubber". It'll then show the best glues/adhesives from best #1 to #5-10 other ones. The design is simple and doesn't need much detail.

Design rules:
Please design using bootstrap 4 with a modified 1440px width.

We're looking for 4 main pages:
Home Page, Compare Page, Category Page, Product Page.

Target Market(s)

Everyone

Industry/Entity Type

Adhesive

Number of Pages Required

3 page

Font styles to use
Sans Serif

Colors
876aae
b7a5cd
6b449b
e4daeb
fefeff

Requirements
Must have
• We like the following features of these designs:
https://pixelvane.example/shots/6401517-CoverLoom-Dashboard - Main menu with the drop down, this will change depending on the active page. If they are on a metal page they could be shown "glue metal to ___" options. We also like the simple table view in this design under "users" heading.

https://pixelvane.example/shots/6300662-Volt-Sketch-Quotation-Page - The entire colour palette is great! The simplicity of the design is great.

https://pixelvane.example/shots/8593973-Loans-Comparison-UI - The boxes at the top look great, if there was 2 of these with a compare icon between them and above that saying "glue metal to rubber" and it shows an icon/image or metal and glue... The table of products is also good, it has dot points and details which we like.

https://pixelvane.example/shots/4586351-Transfer-Money/attachments/4586351-Transfer-Money?mode=media - The right it shows which 2 products are selected (metal and rubber) for example, on the left it would say "best glue for metal and rubber". This is too detailed though, so it would need to be simplified nicely.

https://linquora.example/ - They do a good job of "comparing" 2 things and displaying integrations well. You can get lots of ideas from them linking A to B similar to what we want to show.

https://www.campaignflowreview.example/leadnest-vs-drivemint/ - This shows a good example of the hero section how it should look.

Features of each page to help you design:
Home Page-
Menu (shown in examples above)
Hero section (colour section) with a centre heading saying "what do you want to glue together" with 2 boxes below to select materials from.
List of most popular searches (metal to rubber, glass to wood, fabric to leather... repeat these to fill space).
List of popular products with basic details about each one (grid format, not list).
FAQs - You choose design for this
Content section (simple design, headings, paragraphs, dotpoints, images...)
Blog section - Simple 3 column grid with an image on top, heading, paragraph, button.

Compare Page-
Showing 2 materials in the colour hero section under or to the right of the heading and paragraph.
Best product (highlighted)
9 other products (list table)
3 column section saying glue (product a to ___) with other product that isn't product b + reverse of this.
Content section

Category page-
heading and breadcrumbs in hero section
Standard product list 1 column on the left with filters, 3 products shown on the right in grid format with basic details on each one.

Product page-
Image left, details on the right.
Keep the image smaller not 50% as we want it to not take up too much space vertically.
Under this put a table where this product ranks for gluing things together. for example #3 for gluing metal to rubber, #1 for glass to wood.
Content section.

Please note, keep this design flat, simple and pretty. We don't need it over-designed or detailed, we simply want a simple functionality website that clearly shows what we're looking for.

```html
<!DOCTYPE html>
<html lang="en">
<head>
<meta charset="utf-8">
<title>Glue Compare – Page Designs</title>
<link href="https://fonts.googleapis.com/css2?family=Raleway:wght@400;500;600;700&display=swap" rel="stylesheet">
<style>
:root{
  --purple:#6b449b;
  --purple-mid:#876aae;
  --purple-soft:#b7a5cd;
  --lavender:#e4daeb;
  --white:#fefeff;
  --board:#8a8a8a;
  --section-grey:#f0f0f1;
  --cell-grey:#e6e6e8;
  --text-grey:#777;
  --footer:#383838;
}
*{margin:0;padding:0;box-sizing:border-box}
html,body{width:1200px;height:1200px;overflow:hidden;background:var(--board);font-family:'Raleway',sans-serif}
.board{position:absolute;left:0;top:0;width:1932px;height:1932px;transform:scale(.62112);transform-origin:0 0}
.page{position:absolute;background:var(--white);overflow:hidden}
.abs{position:absolute}
.topnav{position:absolute;top:20px;right:32px;display:flex;gap:16px;font-size:7px;color:var(--text-grey);font-weight:500}
.ph{position:absolute;display:block}
.ph-warm{background:linear-gradient(170deg,#e8cfa6 0%,#c9a27a 45%,#8d6a4c 100%)}
.ph-bottles{background:linear-gradient(180deg,#d9c4a0 0%,#e9e4dc 45%,#9a7a58 100%)}
.ph-yellow{background:linear-gradient(160deg,#f2d44a,#e6b624 60%,#c88f1a)}
.ph-red{background:linear-gradient(160deg,#e5473c,#c81f2a 60%,#f1c232)}
.ph-blue{background:linear-gradient(160deg,#2f6cc4,#d8e4f2 55%,#e23a33)}
.ph-green{background:linear-gradient(160deg,#2f8a3a,#1c4d24 60%,#c93a3a)}
.ph-lime{background:linear-gradient(160deg,#e4e04a,#8bc43f 55%,#2c3e50)}
.ph-orange{background:linear-gradient(160deg,#f08a3c,#f4f1ee 55%,#e06a2a)}
.ph-metal{background:linear-gradient(160deg,#e9e9ea,#8d8f93 45%,#d6d7d9 70%,#5b5d61)}
.ph-rubber{background:linear-gradient(160deg,#5a5a5a,#2a2a2a 55%,#4a4a4a)}
.ph-wood{background:linear-gradient(90deg,#d08a3c,#e9a654 35%,#c27a30 70%,#dd9a48)}
.ph-leather{background:linear-gradient(160deg,#b86a35,#8e4a22 60%,#a85c2c)}
.ph-dark{background:linear-gradient(180deg,#6a5846,#3a3028 60%,#2c2620)}
.ph-navy{background:linear-gradient(120deg,#1b1f6e 0%,#23239a 45%,#3a1f8a 75%,#18207a 100%)}
.section{position:absolute;left:0;width:100%}
.sec-title{position:absolute;left:0;width:100%;text-align:center;color:var(--purple);font-size:14px;font-weight:500}
.lead{position:absolute;text-align:center;color:var(--purple-mid);font-size:6px;line-height:10px}
.btn{position:absolute;background:var(--purple);color:#fff;font-size:5.5px;font-weight:700;letter-spacing:.4px;display:flex;align-items:center;justify-content:center;text-transform:uppercase;border-radius:1px}
.btn-outline{background:#fff;color:#444;border:1px solid #555}
.card{position:absolute;background:#fff}
.card-shadow{box-shadow:0 0 0 1px #dcdcdc}
.ctitle{position:absolute;left:0;width:100%;text-align:center;font-size:9px;color:var(--purple-mid)}
.price{position:absolute;left:0;width:100%;text-align:center;font-size:7px;color:var(--purple-mid)}
.small{position:absolute;font-size:6px;line-height:10px;color:var(--purple-mid)}
.mat-title{position:absolute;font-size:11.5px;color:var(--purple-mid);font-weight:500;line-height:14px}
.btitle{position:absolute;left:13px;font-size:9px;font-weight:700;color:var(--purple);letter-spacing:.2px}
.bprice{position:absolute;left:13px;font-size:10px;color:var(--purple);font-weight:500}
.contact-title{position:absolute;left:0;width:100%;text-align:center;color:#fff;font-size:19px;font-weight:600;letter-spacing:2.5px}
.biz{position:absolute;color:#fff;font-size:13px;font-weight:400}
.biz-line{position:absolute;color:#fff;font-size:6px;opacity:.9}
.field{position:absolute;background:#fff;font-size:6px;color:#aaa;padding:4px 5px}
.socials{position:absolute;display:flex;gap:8px}
.socials span{width:8px;height:8px;border-radius:50%;background:#fff;display:block}
.ring{position:absolute;border-radius:50%;border:1px solid #ddd;overflow:hidden;background:#fff}
.headline-tag{position:absolute;background:#fff;color:var(--purple);font-size:8px;font-weight:700;text-align:center;line-height:12px}
.learn{position:absolute;left:0;width:100%;text-align:center;font-size:6px;color:var(--purple-mid);text-decoration:underline}
</style>
</head>
<body>
<div class="board">

<section class="page page-home" style="left:50px;top:60px;width:503px;height:1713px">
  <nav class="topnav"><span>Home</span><span>Compare</span><span>Category</span><span>Product</span></nav>
  <div class="ph ph-bottles" role="img" aria-label="Hero photo of assorted glue bottles on a wooden table" style="left:28px;top:31px;width:447px;height:240px"></div>
  <svg class="abs" style="left:6px;top:175px" width="14" height="24"><path d="M11 1 L2 12 L11 23" fill="none" stroke="#999" stroke-width="1.2"/></svg>
  <svg class="abs" style="left:483px;top:175px" width="14" height="24"><path d="M3 1 L12 12 L3 23" fill="none" stroke="#999" stroke-width="1.2"/></svg>
  <div class="abs" style="left:120px;top:230px;width:263px;height:52px;background:#fff"></div>
  <h1 class="abs" style="left:0;top:252px;width:503px;text-align:center;font-size:22px;font-weight:500;color:var(--purple)">Best glue webpage</h1>
  <p class="lead" style="left:141px;top:286px;width:220px">Lorem ipsum dolor sit amet, consectetur adipiscing elit. Sed tempor nisi risus, at euismod mi volutpat non.</p>
  <div class="abs" style="left:238px;top:315px;width:10px;height:1px;background:#999"></div>
  <div class="abs" style="left:252px;top:315px;width:10px;height:1px;background:#999"></div>

  <div class="section" style="top:343px;height:292px;background:var(--section-grey)">
    <h2 class="sec-title" style="top:23px">What do you want to glue together?</h2>
    <p class="lead" style="left:40px;top:48px;width:423px">Lorem ipsum dolor sit amet, consectetur adipiscing elit. Sed tempor nisi risus, at euismod mi volutpat non. Aliquam felis elit</p>
    <div class="ph ph-metal" role="img" aria-label="Photo of stacked metal tubes" style="left:39px;top:77px;width:123px;height:97px"></div>
    <div class="ph ph-rubber" role="img" aria-label="Photo of rubber tyres" style="left:190px;top:77px;width:123px;height:97px"></div>
    <div class="ph ph-blue" role="img" aria-label="Photo of a super glue pack" style="left:340px;top:77px;width:123px;height:97px;box-shadow:0 0 0 1px #ccc"></div>
    <div class="mat-title" style="left:39px;top:183px">Metal</div>
    <div class="mat-title" style="left:190px;top:183px">Rubber</div>
    <div class="mat-title" style="left:340px;top:183px;width:120px">Best glue for metal and rubber</div>
    <p class="small" style="left:39px;top:204px;width:125px">Lorem ipsum dolor sit amet, consectetur adipiscing elit. Sed tempor nisi risus, at euismod mi volutpat non</p>
    <p class="small" style="left:190px;top:204px;width:125px">Lorem ipsum dolor sit amet, consectetur adipiscing elit. Sed tempor nisi risus, at euismod mi volutpat non</p>
    <p class="small" style="left:340px;top:218px;width:125px">Lorem ipsum dolor sit amet, consectetur adipiscing elit. Sed tempor nisi risus, at euismod mi volutpat non</p>
    <div class="btn" style="left:67px;top:244px;width:75px;height:15px;text-transform:none;font-weight:500">Select material&nbsp;⌄</div>
    <div class="btn" style="left:215px;top:244px;width:73px;height:15px;text-transform:none;font-weight:500">Select material&nbsp;⌄</div>
    <div class="btn btn-outline" style="left:379px;top:254px;width:46px;height:16px">Show more ↓</div>
  </div>

  <div class="section" style="top:635px;height:302px">
    <div class="ph ph-warm" role="img" aria-label="Blurred background photo of glue bottles on a wooden table" style="left:0;top:0;width:100%;height:100%"></div>
    <h2 class="abs" style="left:28px;top:16px;font-size:14px;font-weight:500;color:var(--purple)">Most popular searches</h2>
    <div class="card" style="left:28px;top:50px;width:140px;height:223px">
      <div class="ctitle" style="top:12px">Product 1 Title</div>
      <div class="ring" style="left:18px;top:31px;width:104px;height:104px"><div class="ph ph-red" role="img" aria-label="Super glue pack" style="left:27px;top:4px;width:50px;height:96px"></div></div>
      <div class="price" style="top:148px">$9.95</div>
      <p class="small" style="left:12px;top:164px;width:116px;text-align:center">Sample small text. Lorem ipsum dolor sit amet.</p>
      <div class="btn" style="left:39px;top:194px;width:63px;height:15px">Add to cart</div>
    </div>
    <div class="card" style="left:181px;top:50px;width:140px;height:223px">
      <div class="ctitle" style="top:12px">Product 2 Title</div>
      <div class="ring" style="left:18px;top:31px;width:104px;height:104px"><div class="ph ph-yellow" role="img" aria-label="Glue remover can" style="left:27px;top:4px;width:50px;height:96px"></div></div>
      <div class="price" style="top:148px">$9.95</div>
      <p class="small" style="left:12px;top:164px;width:116px;text-align:center">Sample small text. Lorem ipsum dolor sit amet.</p>
      <div class="btn" style="left:39px;top:194px;width:63px;height:15px">Add to cart</div>
    </div>
    <div class="card" style="left:334px;top:50px;width:140px;height:223px">
      <div class="ctitle" style="top:12px">Product 3 Title</div>
      <div class="ring" style="left:18px;top:31px;width:104px;height:104px"><div class="ph ph-blue" role="img" aria-label="Super glue pack" style="left:27px;top:4px;width:50px;height:96px"></div></div>
      <div class="price" style="top:148px">$9.95</div>
      <p class="small" style="left:12px;top:164px;width:116px;text-align:center">Sample small text. Lorem ipsum dolor sit amet.</p>
      <div class="btn" style="left:39px;top:194px;width:63px;height:15px">Add to cart</div>
    </div>
  </div>

  <div class="section" style="top:937px;height:491px;background:var(--section-grey)">
    <h2 class="sec-title" style="top:17px">Popular products</h2>
    <div class="card" style="left:28px;top:46px;width:145px;height:207px;background:var(--cell-grey)">
      <div class="ph" style="left:11px;top:11px;width:123px;height:121px;background:#fff;box-shadow:0 1px 2px #bbb"><div class="ph ph-red" role="img" aria-label="Super glue pack" style="left:40px;top:6px;width:45px;height:108px"></div></div>
      <div class="ctitle" style="top:140px">Product 1 Title</div><div class="price" style="top:160px">$9.95</div>
      <div class="btn" style="left:40px;top:180px;width:64px;height:15px">Add to cart</div>
    </div>
    <div class="card" style="left:179px;top:46px;width:145px;height:207px;background:var(--cell-grey)">
      <div class="ph" style="left:11px;top:11px;width:123px;height:121px;background:#fff;box-shadow:0 1px 2px #bbb"><div class="ph ph-lime" role="img" aria-label="Gel glue pack" style="left:30px;top:6px;width:64px;height:108px"></div></div>
      <div class="ctitle" style="top:140px">Product 2 Title</div><div class="price" style="top:160px">$9.95</div>
      <div class="btn" style="left:40px;top:180px;width:64px;height:15px">Add to cart</div>
    </div>
    <div class="card" style="left:329px;top:46px;width:145px;height:207px;background:var(--cell-grey)">
      <div class="ph" style="left:11px;top:11px;width:123px;height:121px;background:#fff;box-shadow:0 1px 2px #bbb"><div class="ph ph-yellow" role="img" aria-label="Super glue pack" style="left:30px;top:6px;width:64px;height:108px"></div></div>
      <div class="ctitle" style="top:140px">Product 3 Title</div><div class="price" style="top:160px">$9.95</div>
      <div class="btn" style="left:40px;top:180px;width:64px;height:15px">Add to cart</div>
    </div>
    <div class="card" style="left:28px;top:259px;width:145px;height:207px;background:var(--cell-grey)">
      <div class="ph" style="left:11px;top:11px;width:123px;height:121px;background:#fff;box-shadow:0 1px 2px #bbb"><div class="ph ph-yellow" role="img" aria-label="Glue remover can" style="left:30px;top:4px;width:64px;height:112px"></div></div>
      <div class="ctitle" style="top:140px">Product 3 Title</div><div class="price" style="top:160px">$9.95</div>
      <div class="btn" style="left:40px;top:180px;width:64px;height:15px">Add to cart</div>
    </div>
    <div class="card" style="left:179px;top:259px;width:145px;height:207px;background:var(--cell-grey)">
      <div class="ph" style="left:11px;top:11px;width:123px;height:121px;background:#fff;box-shadow:0 1px 2px #bbb"><div class="ph ph-blue" role="img" aria-label="Super glue pack" style="left:30px;top:4px;width:64px;height:112px"></div></div>
      <div class="ctitle" style="top:140px">Product 3 Title</div><div class="price" style="top:160px">$9.95</div>
      <div class="btn" style="left:40px;top:180px;width:64px;height:15px">Add to cart</div>
    </div>
    <div class="card" style="left:329px;top:259px;width:145px;height:207px;background:var(--cell-grey)">
      <div class="ph" style="left:11px;top:11px;width:123px;height:121px;background:#fff;box-shadow:0 1px 2px #bbb"><div class="ph ph-orange" role="img" aria-label="Pack of small glue tubes" style="left:22px;top:4px;width:80px;height:112px"></div></div>
      <div class="ctitle" style="top:140px">Product 3 Title</div><div class="price" style="top:160px">$9.95</div>
      <div class="btn" style="left:40px;top:180px;width:64px;height:15px">Add to cart</div>
    </div>
  </div>

  <div class="section" style="top:1428px;height:232px">
    <div class="ph ph-dark" role="img" aria-label="Dimmed background photo of glue bottles" style="left:0;top:0;width:100%;height:100%"></div>
    <h2 class="contact-title" style="top:26px">CONTACT US</h2>
    <div class="biz" style="left:75px;top:85px">Business Center</div>
    <div class="biz-line" style="left:75px;top:110px">48 Harlow Ave, Brookmere, NY 10422</div>
    <div class="biz-line" style="left:75px;top:128px">1 555-014-2290</div>
    <div class="biz-line" style="left:75px;top:146px;color:var(--purple-soft)">contacts@brookmere.example</div>
    <div class="socials" style="left:78px;top:168px"><span></span><span></span><span></span><span></span></div>
    <div class="field" style="left:247px;top:74px;width:190px;height:16px">Name</div>
    <div class="field" style="left:247px;top:97px;width:190px;height:16px">Email</div>
    <div class="field" style="left:247px;top:120px;width:190px;height:47px">Address</div>
    <div class="btn" style="left:247px;top:175px;width:49px;height:15px">Submit</div>
  </div>
  <footer class="section" style="top:1660px;height:53px;background:var(--footer)">
    <p class="abs" style="left:150px;top:20px;width:203px;text-align:center;font-size:5.5px;line-height:9px;color:#bbb">Sample text. Click to select the text box. Click again or double click to start editing the text.</p>
  </footer>
</section>

<section class="page page-compare" style="left:665px;top:60px;width:537px;height:1520px">
  <nav class="topnav"><span>Home</span><span>Compare</span><span>Category</span><span>Product</span></nav>
  <div class="ph" role="img" aria-label="Photo of yellow-capped super glue bottles" style="left:29px;top:40px;width:237px;height:251px;background:linear-gradient(170deg,#9a8a5a,#c8a83a 40%,#6a5a3a)"></div>
  <div class="abs" style="left:54px;top:141px;color:#fff;font-size:15px;font-weight:500">Compare Page</div>
  <p class="abs" style="left:54px;top:168px;width:175px;color:#fff;font-size:6px;line-height:10px">Lorem ipsum dolor sit amet, consectetur adipiscing elit. Lorem ipsum dolor sit amet.</p>
  <div class="ph ph-yellow" role="img" aria-label="Row of super glue packs" style="left:270px;top:40px;width:237px;height:123px;box-shadow:0 0 0 1px #ccc"></div>
  <div class="ph" role="img" aria-label="Row of glue remover cans" style="left:270px;top:168px;width:237px;height:123px;box-shadow:0 0 0 1px #ccc;background:linear-gradient(180deg,#fff 0,#fff 8%,#f2d44a 10%,#e6b624 90%,#fff 92%)"></div>

  <div class="section" style="top:328px;height:324px;background:var(--section-grey)">
    <h2 class="sec-title" style="top:17px">Best Products</h2>
    <div class="card card-shadow" style="left:29px;top:47px;width:155px;height:230px">
      <div class="ph ph-yellow" role="img" aria-label="Glue remover can" style="left:42px;top:15px;width:70px;height:122px"></div>
      <div class="btitle" style="top:150px">PRODUCT 1 TITLE</div>
      <p class="small" style="left:13px;top:168px;width:130px;color:#555">Sample small text. Lorem ipsum dolor sit amet.</p>
      <div class="bprice" style="top:203px">$9.95</div>
      <div class="btn" style="left:79px;top:200px;width:63px;height:17px">Add to cart</div>
    </div>
    <div class="card card-shadow" style="left:191px;top:47px;width:155px;height:230px">
      <div class="ph ph-yellow" role="img" aria-label="Super glue pack" style="left:42px;top:15px;width:70px;height:122px"></div>
      <div class="btitle" style="top:150px">PRODUCT 2 TITLE</div>
      <p class="small" style="left:13px;top:168px;width:130px;color:#555">Sample small text. Lorem ipsum dolor sit amet.</p>
      <div class="bprice" style="top:203px">$9.95</div>
      <div class="btn" style="left:79px;top:200px;width:63px;height:17px">Add to cart</div>
    </div>
    <div class="card card-shadow" style="left:352px;top:47px;width:155px;height:230px">
      <div class="ph ph-lime" role="img" aria-label="Gel glue pack" style="left:42px;top:22px;width:70px;height:112px"></div>
      <div class="btitle" style="top:150px">PRODUCT 3 TITLE</div>
      <p class="small" style="left:13px;top:168px;width:130px;color:#555">Sample small text. Lorem ipsum dolor sit amet.</p>
      <div class="bprice" style="top:203px">$9.95</div>
      <div class="btn" style="left:79px;top:200px;width:63px;height:17px">Add to cart</div>
    </div>
  </div>

  <div class="section" style="top:652px;height:619px;background:#ececed">
    <h2 class="sec-title" style="top:17px">Other products</h2>
    <div class="card card-shadow" style="left:29px;top:41px;width:155px;height:177px"><div class="ph ph-red" role="img" aria-label="Three super glue packs" style="left:12px;top:15px;width:131px;height:80px"></div><div class="ctitle" style="top:106px">Product 1 Title</div><div class="price" style="top:127px">$9.95</div><div class="btn" style="left:43px;top:148px;width:69px;height:16px">Add to cart</div></div>
    <div class="card card-shadow" style="left:191px;top:41px;width:155px;height:177px"><div class="ph" role="img" aria-label="Three super glue packs" style="left:12px;top:15px;width:131px;height:80px;background:linear-gradient(160deg,#f1e04a,#d8342a 70%)"></div><div class="ctitle" style="top:106px">Product 2 Title</div><div class="price" style="top:127px">$9.95</div><div class="btn" style="left:43px;top:148px;width:69px;height:16px">Add to cart</div></div>
    <div class="card card-shadow" style="left:352px;top:41px;width:155px;height:177px"><div class="ph ph-green" role="img" aria-label="Three glue tube packs" style="left:12px;top:15px;width:131px;height:80px"></div><div class="ctitle" style="top:106px">Product 3 Title</div><div class="price" style="top:127px">$9.95</div><div class="btn" style="left:43px;top:148px;width:69px;height:16px">Add to cart</div></div>
    <div class="card card-shadow" style="left:29px;top:224px;width:155px;height:177px"><div class="ph ph-blue" role="img" aria-label="Three super glue packs" style="left:12px;top:15px;width:131px;height:80px"></div><div class="ctitle" style="top:106px">Product 3 Title</div><div class="price" style="top:127px">$9.95</div><div class="btn" style="left:43px;top:148px;width:69px;height:16px">Add to cart</div></div>
    <div class="card card-shadow" style="left:191px;top:224px;width:155px;height:177px"><div class="ph ph-lime" role="img" aria-label="Three gel glue packs" style="left:12px;top:15px;width:131px;height:80px"></div><div class="ctitle" style="top:106px">Product 3 Title</div><div class="price" style="top:127px">$9.95</div><div class="btn" style="left:43px;top:148px;width:69px;height:16px">Add to cart</div></div>
    <div class="card card-shadow" style="left:352px;top:224px;width:155px;height:177px"><div class="ph ph-orange" role="img" aria-label="Three packs of small glue tubes" style="left:12px;top:15px;width:131px;height:80px"></div><div class="ctitle" style="top:106px">Product 3 Title</div><div class="price" style="top:127px">$9.95</div><div class="btn" style="left:43px;top:148px;width:69px;height:16px">Add to cart</div></div>
    <div class="card card-shadow" style="left:29px;top:407px;width:155px;height:178px"><div class="ph ph-yellow" role="img" aria-label="Three glue remover cans" style="left:12px;top:15px;width:131px;height:80px"></div><div class="ctitle" style="top:106px">Product 1 Title</div><div class="price" style="top:127px">$17.00</div><div class="btn" style="left:43px;top:148px;width:69px;height:16px">Add to cart</div></div>
    <div class="card card-shadow" style="left:191px;top:407px;width:155px;height:178px"><div class="ph ph-yellow" role="img" aria-label="Row of super glue packs" style="left:12px;top:15px;width:131px;height:80px"></div><div class="ctitle" style="top:106px">Product 2 Title</div><div class="price" style="top:127px">$245.00</div><div class="btn" style="left:43px;top:148px;width:69px;height:16px">Add to cart</div></div>
    <div class="card card-shadow" style="left:352px;top:407px;width:155px;height:178px"><div class="ph" role="img" aria-label="Three packs of glue tubes" style="left:12px;top:15px;width:131px;height:80px;background:linear-gradient(160deg,#e6eef8,#3a78c8 60%,#e6eef8)"></div><div class="ctitle" style="top:106px">Product 3 Title</div><div class="price" style="top:127px">$19.00</div><div class="btn" style="left:43px;top:148px;width:69px;height:16px">Add to cart</div></div>
  </div>

  <div class="section" style="top:1271px;height:249px">
    <div class="ph ph-navy" role="img" aria-label="Abstract navy and purple background with flowing shapes" style="left:0;top:0;width:100%;height:100%"></div>
    <h2 class="contact-title" style="top:28px">CONTACT US</h2>
    <div class="biz" style="left:79px;top:91px">Business Center</div>
    <div class="biz-line" style="left:79px;top:117px">48 Harlow Ave, Brookmere, NY 10422</div>
    <div class="biz-line" style="left:79px;top:136px">1 555-014-2290</div>
    <div class="biz-line" style="left:79px;top:155px;color:var(--purple-soft)">contacts@brookmere.example</div>
    <div class="socials" style="left:83px;top:179px"><span></span><span></span><span></span><span></span></div>
    <div class="field" style="left:264px;top:78px;width:203px;height:18px">Name</div>
    <div class="field" style="left:264px;top:103px;width:203px;height:18px">Email</div>
    <div class="field" style="left:264px;top:128px;width:203px;height:49px">Address</div>
    <div class="btn" style="left:264px;top:186px;width:53px;height:17px">Submit</div>
  </div>
</section>

<section class="page page-materials" style="left:1314px;top:60px;width:538px;height:1176px">
  <nav class="topnav"><span>Home</span><span>Compare</span><span>Category</span><span>Product</span></nav>
  <div class="section" style="top:34px;height:347px;background:var(--section-grey)">
    <h2 class="sec-title" style="top:11px;font-size:13px">Compare Page</h2>
    <p class="lead" style="left:20px;top:35px;width:498px;font-size:7px">Sample large text. Lorem ipsum dolor sit amet, consectetur adipiscing elit nullam nunc justo sagittis suscipit ultrices.</p>
    <div class="ph" role="img" aria-label="Row of glue tube packs" style="left:30px;top:61px;width:237px;height:252px;background:linear-gradient(160deg,#bdbdbd 0,#bdbdbd 12%,#2f8a3a 14%,#1c4d24 70%,#c93a3a 90%,#bdbdbd 95%)"></div>
    <div class="ph ph-lime" role="img" aria-label="Three gel glue packs" style="left:271px;top:61px;width:237px;height:123px;box-shadow:0 0 0 1px #ccc"></div>
    <div class="ph" role="img" aria-label="Three glue tube packs" style="left:271px;top:189px;width:237px;height:124px;box-shadow:0 0 0 1px #ccc;background:linear-gradient(180deg,#fff,#1c1c1c 12%,#2f8a3a 50%,#c93a3a 90%,#fff)"></div>
  </div>
  <div class="section" style="top:381px;height:271px;background:#e8e8ea">
    <div class="card card-shadow" style="left:30px;top:21px;width:155px;height:229px">
      <div class="ph ph-red" role="img" aria-label="Super glue pack" style="left:45px;top:18px;width:66px;height:118px"></div>
      <div class="btitle" style="top:150px">PRODUCT 1 TITLE</div>
      <p class="small" style="left:13px;top:169px;width:130px">Sample small text. Lorem ipsum dolor sit amet.</p>
      <div class="bprice" style="top:203px">$9.95</div>
      <div class="btn" style="left:79px;top:200px;width:63px;height:17px">Add to cart</div>
    </div>
    <div class="card card-shadow" style="left:191px;top:21px;width:155px;height:229px">
      <div class="ph ph-blue" role="img" aria-label="Gel super glue pack" style="left:45px;top:18px;width:66px;height:118px"></div>
      <div class="btitle" style="top:150px">PRODUCT 2 TITLE</div>
      <p class="small" style="left:13px;top:169px;width:130px">Sample small text. Lorem ipsum dolor sit amet.</p>
      <div class="bprice" style="top:203px">$9.95</div>
      <div class="btn" style="left:79px;top:200px;width:63px;height:17px">Add to cart</div>
    </div>
    <div class="card card-shadow" style="left:352px;top:21px;width:156px;height:229px">
      <div class="ph" role="img" aria-label="Super glue pack" style="left:45px;top:18px;width:66px;height:118px;background:linear-gradient(160deg,#f1e04a,#f4f0e0 40%,#d8342a 85%)"></div>
      <div class="btitle" style="top:150px">PRODUCT 3 TITLE</div>
      <p class="small" style="left:13px;top:169px;width:130px">Sample small text. Lorem ipsum dolor sit amet.</p>
      <div class="bprice" style="top:203px">$9.95</div>
      <div class="btn" style="left:79px;top:200px;width:63px;height:17px">Add to cart</div>
    </div>
  </div>
  <div class="section" style="top:652px;height:276px;background:var(--white)">
    <h2 class="sec-title" style="top:24px;font-size:12px">Glue (product a to) with other product that isn't product b + reverse of this</h2>
    <div class="ph ph-wood" role="img" aria-label="Photo of wood grain" style="left:42px;top:60px;width:135px;height:116px"></div>
    <div class="headline-tag" style="left:56px;top:166px;width:107px">Sample Headline</div>
    <p class="small" style="left:62px;top:186px;width:95px;text-align:center">Sample text. Click to select the text box. Click again or double click to start editing the text.</p>
    <div class="learn" style="left:42px;width:135px;top:237px">learn more</div>
    <div class="ph ph-leather" role="img" aria-label="Photo of brown leather" style="left:202px;top:60px;width:134px;height:116px"></div>
    <div class="headline-tag" style="left:215px;top:166px;width:107px">Sample Headline</div>
    <p class="small" style="left:221px;top:186px;width:95px;text-align:center">Sample text. Click to select the text box. Click again or double click to start editing the text.</p>
    <div class="learn" style="left:202px;width:134px;top:237px">learn more</div>
    <div class="ph ph-metal" role="img" aria-label="Photo of stacked metal tubes" style="left:361px;top:60px;width:135px;height:116px"></div>
    <div class="headline-tag" style="left:375px;top:166px;width:107px">Sample Headline</div>
    <p class="small" style="left:381px;top:186px;width:95px;text-align:center">Sample text. Click to select the text box. Click again or double click to start editing the text.</p>
    <div class="learn" style="left:361px;width:135px;top:237px">learn more</div>
  </div>
  <div class="section" style="top:928px;height:248px">
    <div class="ph ph-navy" role="img" aria-label="Abstract navy and purple background with flowing shapes" style="left:0;top:0;width:100%;height:100%"></div>
    <h2 class="contact-title" style="top:28px">CONTACT US</h2>
    <div class="biz" style="left:80px;top:90px">Business Center</div>
    <div class="biz-line" style="left:80px;top:117px">48 Harlow Ave, Brookmere, NY 10422</div>
    <div class="biz-line" style="left:80px;top:136px">1 555-014-2290</div>
    <div class="biz-line" style="left:80px;top:155px;color:var(--purple-soft)">contacts@brookmere.example</div>
    <div class="socials" style="left:84px;top:179px"><span></span><span></span><span></span><span></span></div>
    <div class="field" style="left:264px;top:79px;width:204px;height:17px">Name</div>
    <div class="field" style="left:264px;top:103px;width:204px;height:18px">Email</div>
    <div class="field" style="left:264px;top:128px;width:204px;height:50px">Address</div>
    <div class="btn" style="left:264px;top:187px;width:53px;height:15px">Submit</div>
  </div>
</section>

</div>
</body>
</html>
```